New App Design Project

We are having an app built and require the following:

App Icons
120x120 - iphone/ipod touch - HD
76x76 - iPad
152x152 - iPad - HD

AppStore Icon
1024x1024 PNG

Launch Screen
320x480 - iphone/ipod touch
640x960 - iPhone/iPod touch - HD
768x1004 - iPad (Portrait)
1024x748 - iPad (Landscape)
1536x2008 - iPad (Portrait) = HD
2048x1496 - iPad (Landscape) -HD

ALSO NEED

WELCOME PAGE AND CONTACT US PAGE - STATIC WITH CLICKABLE LINKS for an example of what we want please view the uPage app in the quillbox store.

Text for use in the welcome screen

Welcome to the Marrowby EBook App

The Marrowby App allows you to easily read and navigate monthly updated Ebooks.

From the comfort of you mobile device you can electronically flip through our latest listings from both For Sale and Rental Properties.

Visit our Ebooks:

Residential Properties FOR SALE

Residential Properties suited for INVESTORS

Residential Properties FOR RENT

 

A little about Marrowby…

When you list your property exclusively with Marrowby, we guarantee to advertise it totally free of charge – whether it is sold or withdrawn from the market.

We call it the Marrowby Keystone Marketing Strategy. It’s an approach we’ve researched and designed to generate as many enquiries as possible.

We stand by our reputation for providing a superior service and delivering results – across six offices, seven days a week.

That’s why a third of all property sellers on the northern Gold Coast choose Marrowby as their exclusive agent.

With the wide reaching effects of the Marrowby Keystone Marketing Strategy and over 40 sales people working together to sell your property, you’ll be making the right move with Marrowby.

Industry/Entity Type

Landscape

Requirements
Must have
• Our company logo

```html
<!DOCTYPE html>
<html lang="en">
<head>
<meta charset="utf-8">
<title>Marrowby EBook App – Contact Us</title>
<link rel="stylesheet" href="https://fonts.googleapis.com/css2?family=Open+Sans:wght@400&display=swap">
<style>
  :root {
    --red-deep: #7f1112;
    --red-mid: #a81b1c;
    --red-glow: #d8302d;
    --icon-red: #c4161c;
    --white: #ffffff;
    --rule: rgba(255, 255, 255, 0.55);
  }
  html, body {
    margin: 0;
    padding: 0;
    width: 1200px;
    height: 900px;
    overflow: hidden;
  }
  .screen {
    position: relative;
    width: 1200px;
    height: 900px;
    overflow: hidden;
    background: radial-gradient(ellipse 70% 65% at 50% 62%, var(--red-glow) 0%, var(--red-mid) 48%, var(--red-deep) 100%);
    font-family: "Open Sans", Arial, sans-serif;
    color: var(--white);
  }
  .app-mark {
    position: absolute;
    left: 126px;
    top: 176px;
    width: 300px;
    height: 300px;
  }
  .brand-name {
    position: absolute;
    left: 448px;
    top: 148px;
    margin: 0;
    font-size: 132px;
    font-weight: 400;
    line-height: 1;
    letter-spacing: -1px;
  }
  .app-title {
    position: absolute;
    left: 462px;
    top: 334px;
    margin: 0;
    font-size: 108px;
    font-weight: 400;
    line-height: 1;
    letter-spacing: -1px;
  }
  .divider {
    position: absolute;
    left: 100px;
    top: 546px;
    width: 1000px;
    height: 2px;
    background: linear-gradient(90deg, transparent 0%, var(--rule) 20%, var(--rule) 80%, transparent 100%);
  }
  .page-title {
    position: absolute;
    left: 0;
    top: 582px;
    width: 1200px;
    margin: 0;
    text-align: center;
    font-size: 162px;
    font-weight: 400;
    line-height: 1;
    letter-spacing: 1px;
  }
</style>
</head>
<body>
  <main class="screen">
    <svg class="app-mark" viewBox="0 0 300 300" aria-hidden="true">
      <rect x="6" y="6" width="288" height="288" rx="56" fill="var(--white)"/>
      <rect x="18" y="18" width="264" height="264" rx="46" fill="var(--icon-red)"/>
    </svg>
    <h1 class="brand-name">marrowby</h1>
    <p class="app-title">EBook App</p>
    <div class="divider"></div>
    <h2 class="page-title">CONTACT US</h2>
  </main>
</body>
</html>
```